Modern and Improved business card design for Family Dental Practice

We have 2 sets of logo we have designed and now just need a business card layout and design for the office. Colors are on the logo. We can choose which logo we want to go with . The font can be changed to whatever seems modern and relevant. We are family dental office that has been open for over 15 years in South Austin Texas.

Target Market(s)

Handout Business cards to referrals and specialists

Industry/Entity Type

Dental

Contact Information for Business Card

We need address, phone, website and email address. 4830 North Maple Loop Suite 208 , Austin,Texas 78392....phone: 512-847-3195.....email- info@bluepinedental.example....website - BluePineDental.example

Font styles to use
Serif
Decorative

Requirements
Must have
• my logo. We have 2 logos, but we can use just one or if we can incorporate one on one side and the other on the other side.
Nice to have
• Really just need a modern look and clean that incorporates the logo and colors .

```html
<!DOCTYPE html>
<html lang="en">
<head>
<meta charset="utf-8">
<title>Blue Pine Family Dentistry – Business Card</title>
<link href="https://fonts.googleapis.com/css2?family=Quicksand:wght@500;600;700&display=swap" rel="stylesheet">
<style>
  :root {
    --page-bg: #e9e6df;
    --card-white: #fbfbf7;
    --green-light: #c5cc86;
    --green-mid: #b1bb68;
    --green-deep: #a6b25a;
    --brand-green: #1f8a3b;
    --title-green: #4a983a;
    --text-dark: #3a3a3a;
    --text-muted: #555;
    --rule: #6f6f6f;
    --box: #5aa34a;
  }
  * { box-sizing: border-box; margin: 0; padding: 0; }
  html, body { width: 900px; height: 1200px; overflow: hidden; }
  body {
    background: var(--page-bg);
    font-family: "Quicksand", "Nunito", sans-serif;
    color: var(--text-dark);
    position: relative;
  }
  .card {
    position: absolute;
    left: 80px;
    width: 742px;
    height: 440px;
    border-radius: 32px;
    box-shadow: 4px 6px 6px rgba(0,0,0,0.45);
    overflow: hidden;
  }
  /* Front */
  .card-front {
    top: 132px;
    background: linear-gradient(to bottom,
      var(--card-white) 0%, var(--card-white) 22%,
      var(--green-light) 42%, var(--green-mid) 70%, var(--green-deep) 100%);
  }
  .brand-name {
    position: absolute;
    left: 162px;
    top: 400px;
    transform: rotate(-90deg);
    transform-origin: left top;
    font-size: 21px;
    font-weight: 500;
    letter-spacing: 3px;
    color: var(--text-dark);
    white-space: nowrap;
  }
  .details { position: absolute; left: 343px; top: 138px; }
  .person-name { font-size: 26px; font-weight: 700; color: var(--brand-green); }
  .person-role { font-size: 15px; font-weight: 500; color: var(--text-muted); margin-top: 6px; }
  .address { font-size: 15px; font-weight: 500; line-height: 20px; margin-top: 27px; }
  .contact-list { list-style: none; margin-top: 30px; font-size: 15.5px; font-weight: 500; }
  .contact-list li { display: flex; align-items: center; height: 22px; }
  .contact-list li:first-child { margin-bottom: 4px; }
  .contact-list svg { width: 14px; height: 14px; margin-right: 10px; fill: var(--brand-green); }

  /* Back */
  .card-back { top: 638px; background: #fff; }
  .appt-title {
    position: absolute; top: 74px; width: 100%;
    text-align: center; font-size: 32px; font-weight: 700; color: var(--title-green);
  }
  .field-label { position: absolute; font-size: 17px; font-weight: 500; color: var(--text-dark); }
  .field-rule { position: absolute; height: 1px; background: var(--rule); }
  .day { position: absolute; top: 266px; display: flex; align-items: center; font-size: 17px; font-weight: 500; color: var(--text-muted); }
  .day .check { width: 20px; height: 20px; border: 1.5px solid var(--box); margin-left: 10px; }
</style>
</head>
<body>

<section class="card card-front">
  <div class="brand-name">Blue Pine Family Dentistry</div>
  <div class="details">
    <h1 class="person-name">Dr. Ravi M Kapoor</h1>
    <p class="person-role">Owner</p>
    <p class="address">4830 North Maple Loop Suite 208 ,<br>Austin,Texas 78392</p>
    <ul class="contact-list">
      <li><svg viewBox="0 0 16 16"><path d="M2 6c0-2 3-3 6-3s6 1 6 3v1h-3V6H5v1H2z"/><path d="M4 8h8l1.5 5h-11z"/></svg>512-847-3195</li>
      <li><svg viewBox="0 0 16 16"><path d="M1 3h14v2L8 9 1 5z"/><path d="M1 7l7 4 7-4v6H1z"/></svg>info@bluepinedental.example</li>
      <li><svg viewBox="0 0 16 16"><circle cx="8" cy="8" r="7"/><path d="M5 4c2 1 1 3 3 4s1 3 0 4M10 3c-1 2 2 2 3 4" stroke="#fff" stroke-width="1.3" fill="none"/></svg>www.BluePineDental.example</li>
    </ul>
  </div>
</section>

<section class="card card-back">
  <h2 class="appt-title">Next Appoinment</h2>

  <span class="field-label" style="left:35px; top:147px;">Name</span>
  <div class="field-rule" style="left:100px; right:37px; top:156px;"></div>

  <span class="field-label" style="left:35px; top:187px;">Date</span>
  <div class="field-rule" style="left:100px; right:37px; top:201px;"></div>

  <div class="day" style="left:35px;">Sun<span class="check"></span></div>
  <div class="day" style="left:132px;">Mon<span class="check"></span></div>
  <div class="day" style="left:238px;">Tue<span class="check"></span></div>
  <div class="day" style="left:330px;">Wed<span class="check"></span></div>
  <div class="day" style="left:437px;">Thu<span class="check"></span></div>
  <div class="day" style="left:547px;">Fri<span class="check"></span></div>
  <div class="day" style="left:642px;">Sat<span class="check"></span></div>

  <span class="field-label" style="left:37px; top:327px;">Note</span>
  <div class="field-rule" style="left:102px; right:35px; top:336px;"></div>
  <div class="field-rule" style="left:36px; right:35px; top:384px;"></div>
</section>

</body>
</html>
```